Business Cards for Orvanta LLC

We need business cards for a new company called “Orvanta LLC”. This is a technology process improvement company providing a comprehensive assessment of the technology used to run their business. The documentation and review process delivers the visibility and reassurance they need to protect their business and plan for the future. The product is called “Systems Mapwork”. Our primary target is small-medium size businesses, with the deliverables going to the decision maker. We would like to see the designs use the color blue. Our tag line is PROTECT YOUR BUSINESS · TAKE CONTROL OF IT.

Industry/Entity Type

Business

Contact Information for Business Card

Tag line should be on back of card - it does not have to be upper case.

Requirements
Must have
• Please use information when laying out card:
• Name: Gareth Pellham
• Title: Partner
• Phone Number: (844)555-0172
• Email: gareth@orvantallc-example.com
• Website: http://orvantallc-example.com

```html
<!DOCTYPE html>
<html lang="en">
<head>
<meta charset="utf-8">
<title>Business Cards for Orvanta LLC</title>
<link rel="stylesheet" href="https://fonts.googleapis.com/css2?family=Arimo:wght@400;700&display=swap">
<style>
  :root {
    --page: #ece9e4;
    --card-light: #eeeeee;
    --card-white: #f7f7f7;
    --brand-blue: #3b62a6;
    --brand-blue-deep: #34589a;
    --steel-grey: #7d7d7d;
    --text-light: #ffffff;
    --text-soft: #dfe6f3;
  }
  * { box-sizing: border-box; margin: 0; padding: 0; }
  html, body { width: 1200px; height: 723px; overflow: hidden; }
  body {
    background: var(--page);
    font-family: "Arimo", Arial, sans-serif;
    display: flex;
    justify-content: center;
    align-items: center;
    gap: 80px;
  }
  .card {
    position: relative;
    width: 344px;
    height: 600px;
    border-radius: 4px;
    overflow: hidden;
    box-shadow: 0 6px 18px rgba(0,0,0,.18);
    background: var(--card-white);
  }

  /* Back */
  .card-back .backdrop { position: absolute; inset: 0; }
  .card-back .tagline {
    position: absolute;
    left: 30px;
    bottom: 48px;
    color: var(--text-light);
    text-transform: uppercase;
  }
  .tagline-main { font-weight: 700; font-size: 19px; letter-spacing: .5px; }
  .tagline-sub { font-size: 17px; margin-top: 4px; color: var(--text-soft); }

  /* Front */
  .card-front .brand-zone {
    height: 226px;
    background: linear-gradient(180deg, var(--card-white), var(--card-light));
    display: flex;
    align-items: center;
    justify-content: center;
    gap: 12px;
  }
  .brand-square { width: 26px; height: 26px; background: var(--brand-blue); }
  .brand-name {
    color: var(--brand-blue);
    font-weight: 700;
    font-size: 34px;
    letter-spacing: 1px;
  }
  .card-front .divider-band { height: 12px; background: var(--steel-grey); }
  .card-front .info-zone {
    position: absolute;
    top: 238px; left: 0; right: 0; bottom: 0;
    background: var(--brand-blue);
    color: var(--text-light);
    text-align: center;
    padding-top: 56px;
  }
  .person-name { font-weight: 700; font-size: 25px; letter-spacing: 1px; text-transform: uppercase; }
  .person-title { font-size: 20px; margin-top: 6px; }
  .rule {
    width: 150px; height: 1px; margin: 26px auto 28px;
    background: linear-gradient(90deg, transparent, var(--text-soft), transparent);
  }
  .contact { list-style: none; font-size: 16px; line-height: 1.75; color: var(--text-soft); }
</style>
</head>
<body>
  <section class="card card-back" aria-label="Card back">
    <svg class="backdrop" width="344" height="600" viewBox="0 0 344 600" aria-hidden="true">
      <rect width="344" height="600" fill="var(--card-light)"/>
      <polygon points="0,250 344,180 344,212 0,282" fill="var(--steel-grey)"/>
      <polygon points="0,282 344,212 344,600 0,600" fill="var(--brand-blue)"/>
    </svg>
    <div class="tagline">
      <p class="tagline-main">Protect your business</p>
      <p class="tagline-sub">Take control of it.</p>
    </div>
  </section>

  <section class="card card-front" aria-label="Card front">
    <div class="brand-zone">
      <span class="brand-square" aria-hidden="true"></span>
      <span class="brand-name">Orvanta LLC</span>
    </div>
    <div class="divider-band"></div>
    <div class="info-zone">
      <h1 class="person-name">Gareth Pellham</h1>
      <p class="person-title">Partner</p>
      <div class="rule"></div>
      <ul class="contact">
        <li>(844)555-0172</li>
        <li>gareth@orvantallc-example.com</li>
        <li>www.orvantallc-example.com</li>
      </ul>
    </div>
  </section>
</body>
</html>
```